Kobalto Cell Phone Repair

We are a small cell phone repair store in need of a redesign to our current business card to make it a more modern, cleaner design that will catch folks' attention (perhaps with rounded edges ) - But still include most of the information listed on the current card. Would like to keep the current color scheme of black/white and green. Card will not need any personnel name included. Would like to see some designs include takes on a velorin or tekvo screen as well as more traditional cards.

Target Market(s)

broad spectrum across all cell phone users

Industry/Entity Type

Cell Phone

Contact Information for Business Card

changes to front text:
keep business Logo
business address, phone number website and email. All other info optional (add gathernest and blurvo icons on card

Rear of card:

Keep repair services, change tekvo repair to slatra repair, change quorvex os repair to data recovery (with appropriate icon or substitute)
remove products text
remove pjw and ravesh from manufacturer logos, add dunbelio.

Requirements
Must have
• business Logo
• business address, phone number website and email
• keep colors to white/black/green/gray
• gathernest and blurvo icons on card
Nice to have
• Would like to see 'traditional' business card design as well as creative design incorporating incorporating front of cell phone (eg tekvo or quorvex). Rounded edges would be nice but not necessary.

```html
<!DOCTYPE html>
<html lang="en">
<head>
<meta charset="utf-8">
<title>Kobalto Cell Phone Repair – Business Card</title>
<link href="https://fonts.googleapis.com/css2?family=Roboto+Condensed:wght@400;700&family=Montserrat:wght@500;700;800&display=swap" rel="stylesheet">
<style>
  :root {
    --page: #e9e9e6;
    --black: #121212;
    --charcoal: #262626;
    --white: #ffffff;
    --green: #6cb33f;
    --green-dark: #4f8f2a;
    --gray: #6b6b6b;
    --gray-light: #cfcfcf;
  }
  * { box-sizing: border-box; margin: 0; padding: 0; }
  html, body { width: 900px; height: 1200px; overflow: hidden; }
  body {
    background: var(--page);
    font-family: "Roboto Condensed", Arial, sans-serif;
    position: relative;
  }
  .card {
    position: absolute;
    left: 70px;
    width: 760px;
    height: 430px;
    border-radius: 18px;
    overflow: hidden;
    box-shadow: 0 6px 18px rgba(0,0,0,.18);
  }
  /* ---------- back side: services ---------- */
  .card-services {
    top: 120px;
    background: radial-gradient(ellipse at 50% 30%, #2e2e2e 0%, var(--black) 70%);
  }
  .services-title {
    position: absolute;
    top: 34px; left: 0; right: 0;
    text-align: center;
    color: var(--white);
    font-family: "Montserrat", Arial, sans-serif;
    font-weight: 800;
    font-size: 26px;
    letter-spacing: .5px;
  }
  .service-list {
    position: absolute;
    top: 92px; left: 30px; right: 30px;
    display: flex;
    justify-content: space-between;
  }
  .service {
    width: 108px;
    text-align: center;
  }
  .service svg { display: block; margin: 0 auto; }
  .service-label {
    margin-top: 12px;
    color: var(--white);
    font-weight: 700;
    font-size: 15px;
    line-height: 1.2;
    text-transform: uppercase;
  }
  .brand-band {
    position: absolute;
    left: 0; right: 0;
    top: 318px; height: 62px;
    background: var(--white);
    display: flex;
    align-items: center;
    justify-content: space-around;
    padding: 0 30px;
  }
  .brand {
    display: flex;
    align-items: center;
    gap: 8px;
    color: var(--gray);
    font-family: "Montserrat", Arial, sans-serif;
    font-weight: 700;
    font-size: 22px;
  }
  .brand-dot {
    width: 14px; height: 14px;
    border-radius: 50%;
    background: var(--green);
  }
  /* ---------- front side: contact ---------- */
  .card-contact {
    top: 640px;
    background: var(--white);
  }
  .logo {
    position: absolute;
    top: 62px; left: 34px;
    display: flex;
    align-items: center;
    gap: 14px;
  }
  .logo-figure {
    width: 96px; height: 150px;
    border-radius: 40px 40px 20px 20px;
    background: linear-gradient(180deg, #8fcf5c 0%, var(--green-dark) 100%);
  }
  .logo-name {
    color: var(--green-dark);
    font-family: "Montserrat", Arial, sans-serif;
    font-weight: 800;
    line-height: 1;
  }
  .logo-name .big { display: block; font-size: 50px; }
  .logo-name .small { display: block; font-size: 20px; margin-top: 8px; letter-spacing: .5px; }
  .divider {
    position: absolute;
    left: 400px; top: 40px;
    width: 2px; height: 220px;
    background: var(--gray-light);
  }
  .contact-list {
    position: absolute;
    left: 428px; top: 44px;
    list-style: none;
  }
  .contact-item {
    display: flex;
    align-items: center;
    gap: 16px;
    height: 70px;
    color: var(--charcoal);
    font-size: 21px;
  }
  .contact-icon {
    width: 38px; height: 38px;
    border-radius: 50%;
    background: var(--gray);
    display: flex; align-items: center; justify-content: center;
  }
  .address-band {
    position: absolute;
    left: 0; right: 0;
    top: 300px; height: 34px;
    background: var(--black);
    color: var(--white);
    text-align: center;
    font-size: 19px;
    line-height: 34px;
    letter-spacing: .3px;
  }
  .offer-band {
    position: absolute;
    left: 0; right: 0;
    top: 334px; bottom: 0;
    background: var(--green);
    color: var(--white);
    padding: 18px 40px 0 40px;
    font-size: 21px;
    line-height: 1.55;
  }
  .offer-band .bullet { margin: 0 8px; }
  .offer-band .inset { padding-left: 16px; }
</style>
</head>
<body>

<section class="card card-services" aria-label="Card back: repair services">
  <h2 class="services-title">CELL PHONE REPAIR SERVICES</h2>
  <div class="service-list">
    <div class="service">
      <svg width="96" height="106" viewBox="0 0 96 106" role="img" aria-label="Photo of a cracked phone screen">
        <polygon points="48,3 93,28 93,78 48,103 3,78 3,28" fill="#5b6f9a" stroke="#fff" stroke-width="3"/>
      </svg>
      <div class="service-label">Cracked<br>Screen</div>
    </div>
    <div class="service">
      <svg width="96" height="106" viewBox="0 0 96 106" role="img" aria-label="Photo of a phone in water">
        <polygon points="48,3 93,28 93,78 48,103 3,78 3,28" fill="#c9b48a" stroke="#fff" stroke-width="3"/>
      </svg>
      <div class="service-label">Water<br>Damage</div>
    </div>
    <div class="service">
      <svg width="96" height="106" viewBox="0 0 96 106" role="img" aria-label="Photo of a phone charging port">
        <polygon points="48,3 93,28 93,78 48,103 3,78 3,28" fill="#9a9a9a" stroke="#fff" stroke-width="3"/>
      </svg>
      <div class="service-label">Charging<br>Port</div>
    </div>
    <div class="service">
      <svg width="96" height="106" viewBox="0 0 96 106" role="img" aria-label="Photo of data recovery on a phone">
        <polygon points="48,3 93,28 93,78 48,103 3,78 3,28" fill="#7bbf4e" stroke="#fff" stroke-width="3"/>
      </svg>
      <div class="service-label">Data<br>Recovery</div>
    </div>
    <div class="service">
      <svg width="96" height="106" viewBox="0 0 96 106" role="img" aria-label="Photo of an unlocked cell phone">
        <polygon points="48,3 93,28 93,78 48,103 3,78 3,28" fill="#8c6fb0" stroke="#fff" stroke-width="3"/>
      </svg>
      <div class="service-label">Cell Phone<br>Unlock</div>
    </div>
    <div class="service">
      <svg width="96" height="106" viewBox="0 0 96 106" role="img" aria-label="Photo of a tablet being repaired">
        <polygon points="48,3 93,28 93,78 48,103 3,78 3,28" fill="#b08a6a" stroke="#fff" stroke-width="3"/>
      </svg>
      <div class="service-label">Slatra<br>Repair</div>
    </div>
  </div>
  <div class="brand-band">
    <span class="brand"><span class="brand-dot"></span>tekvo</span>
    <span class="brand"><span class="brand-dot"></span>velorin</span>
    <span class="brand"><span class="brand-dot"></span>dunbelio</span>
    <span class="brand"><span class="brand-dot"></span>Lumeno</span>
  </div>
</section>

<section class="card card-contact" aria-label="Card front: contact details">
  <div class="logo">
    <div class="logo-figure" role="img" aria-label="Cartoon lizard mascot"></div>
    <div class="logo-name">
      <span class="big">KOBALTO</span>
      <span class="small">CELL PHONE REPAIR</span>
    </div>
  </div>
  <div class="divider"></div>
  <ul class="contact-list">
    <li class="contact-item">
      <span class="contact-icon">
        <svg width="20" height="20" viewBox="0 0 24 24"><path fill="#fff" d="M6.6 10.8a15.1 15.1 0 0 0 6.6 6.6l2.2-2.2c.3-.3.7-.4 1-.2 1.1.4 2.3.6 3.6.6.6 0 1 .4 1 1V20c0 .6-.4 1-1 1A17 17 0 0 1 3 4c0-.6.4-1 1-1h3.5c.6 0 1 .4 1 1 0 1.3.2 2.5.6 3.6.1.3 0 .7-.2 1z"/></svg>
      </span>
      443.555.0174
    </li>
    <li class="contact-item">
      <span class="contact-icon">
        <svg width="22" height="22" viewBox="0 0 24 24" fill="none" stroke="#fff" stroke-width="1.8"><circle cx="12" cy="12" r="9"/><ellipse cx="12" cy="12" rx="4" ry="9"/><path d="M3 12h18M5 7h14M5 17h14"/></svg>
      </span>
      www.kobaltostore.com
    </li>
    <li class="contact-item">
      <span class="contact-icon">
        <svg width="20" height="20" viewBox="0 0 24 24" fill="none" stroke="#fff" stroke-width="2"><rect x="3" y="5" width="18" height="14" rx="1.5"/><path d="M3 6l9 7 9-7"/></svg>
      </span>
      info@kobalto.com
    </li>
  </ul>
  <div class="address-band">1840 Harbor Ave, Easton MD 21601</div>
  <div class="offer-band">
    <div><span class="bullet">•</span>Unlocking &amp; Flashing Service <span class="bullet">•</span>Smart Phones &amp; accessories</div>
    <div class="inset">Water Damage Repair <span class="bullet">•</span>Screen Repair</div>
  </div>
</section>

</body>
</html>
```